Creation of a cover for a book with an image provided. It is mainly a typographical work. PICTURE (Morning Tide II) IS NOW AVAILABLE

Target Market(s)

General Public

Colors

Designer to choose colors to be used in the design.

Requirements
Must have
• Upper edge: "Marisa Kovell" (author) Title: "Every road turns home" Bottom edge: "Pellwick Editions"

```html
<!DOCTYPE html>
<html lang="en">
<head>
<meta charset="utf-8">
<title>Every road turns home — Marisa Kovell</title>
<link rel="stylesheet" href="https://fonts.googleapis.com/css2?family=Josefin+Sans:wght@600;700&family=Cormorant+Garamond:wght@500&display=swap">
<style>
  :root {
    --page-bg: #f1f1f0;
    --cover-navy: #1b2550;
    --cover-white: #f4f4f2;
    --ink-yellow: #f3c04f;
    --ink-teal: #2f9fc0;
    --ink-coral: #ee6a48;
    --ink-pink: #d97a92;
    --ink-slate: #7183ad;
    --ink-green: #5faa8c;
    --paint-red: #e24a2c;
    --paint-orange: #ee7a3c;
    --paint-teal: #4fb8c4;
    --paint-violet: #8b5fb0;
  }
  * { margin: 0; padding: 0; box-sizing: border-box; }
  html, body { width: 1000px; height: 1200px; overflow: hidden; }
  body {
    background: var(--page-bg);
    display: flex;
    align-items: center;
    justify-content: center;
  }
  .book-cover {
    position: relative;
    width: 660px;
    height: 1000px;
    background: var(--cover-navy);
    box-shadow: 0 12px 40px rgba(0,0,0,0.18);
    overflow: hidden;
  }
  .author {
    position: absolute;
    top: 70px;
    width: 100%;
    text-align: center;
    font-family: "Cormorant Garamond", serif;
    font-weight: 500;
    font-size: 30px;
    letter-spacing: 1px;
    color: var(--cover-white);
    text-transform: uppercase;
  }
  .title-frame {
    position: absolute;
    top: 135px;
    left: 28px;
    right: 28px;
    height: 255px;
    padding: 0 24px;
    border: 3px solid var(--cover-white);
    display: flex;
    flex-direction: column;
    align-items: center;
    justify-content: center;
  }
  .title {
    font-family: "Josefin Sans", sans-serif;
    font-weight: 700;
    font-size: 70px;
    line-height: 1.02;
    text-transform: uppercase;
    text-align: center;
    letter-spacing: 1px;
  }
  .title-line { display: block; white-space: nowrap; }
  .c1 { color: var(--ink-yellow); }
  .c2 { color: var(--ink-teal); }
  .c3 { color: var(--ink-coral); }
  .c4 { color: var(--ink-pink); }
  .c5 { color: var(--ink-slate); }
  .c6 { color: var(--ink-green); }
  .cover-artwork {
    position: absolute;
    left: 0;
    right: 0;
    top: 410px;
    bottom: 0;
    background:
      linear-gradient(100deg, rgba(79,184,196,0.85) 0%, rgba(139,95,176,0.6) 35%, rgba(79,184,196,0.75) 65%, rgba(238,200,80,0.6) 100%) top / 100% 30% no-repeat,
      linear-gradient(180deg, var(--paint-teal) 0%, var(--paint-orange) 40%, var(--paint-red) 100%);
  }
  .publisher {
    position: absolute;
    bottom: 70px;
    width: 100%;
    text-align: center;
    font-family: "Cormorant Garamond", serif;
    font-weight: 500;
    font-size: 24px;
    letter-spacing: 1px;
    color: var(--cover-white);
    text-transform: uppercase;
  }
</style>
</head>
<body>
  <main class="book-cover">
    <p class="author">Marisa Kovell</p>
    <div class="title-frame">
      <h1 class="title">
        <span class="title-line"><span class="c1">E</span><span class="c3">v</span><span class="c2">e</span><span class="c4">r</span><span class="c1">y</span> <span class="c5">r</span><span class="c3">o</span><span class="c6">a</span><span class="c2">d</span></span>
        <span class="title-line"><span class="c3">t</span><span class="c2">u</span><span class="c1">r</span><span class="c5">n</span><span class="c4">s</span> <span class="c6">h</span><span class="c1">o</span><span class="c3">m</span><span class="c2">e</span></span>
      </h1>
    </div>
    <div class="cover-artwork" role="img" aria-label="Painting “Morning Tide II”: expressive abstract portrait in vivid orange, red, teal and violet"></div>
    <p class="publisher">Pellwick Editions</p>
  </main>
</body>
</html>
```